THE VELVET NORTH FASHION RE-BRAND

I am having a re-brand of The Velvet North brand to include the website look and feel, and corporate identity.

The brand is defined by its minimal architectural and edgy products and contemporary feel. It is now moving into a slightly more glamorous and higher end market and price point and the branding and look and feel needs to reflect that.

Website Pages

1) Creative and striking artistic Landing page featuring
- main images - slideshow
- other images of collections
- optionalVideo/Sound - Fashion Film
- Instagram Feed

Lookbook/Collections page featuring pictures from fashion weeks of each collection
Press Page
About Page
Product Page
Information Page

The existing website isnt terrible but it needs more stying and a more polished artistic and upmarket feeling without losing its clean and contemporary feeling. This may be achieved using borders or touch of colours or other small detail that will bring everything together.

The existing logo is the just the name which is fine but I am looking for another logo to stand with it which will be a symbol or a repeating pattern using colours black white grey and silver.
Updates

Hi All Here is some website copy for the About Page The Brand Story I want somewhere on the landing page as a scrollable graphic. see brindlecove.com/about/ The rest of it - About Us and Design Ethos will go on a seperte page. Thanks see below text Text for Landing Page We are London. We are every cool city in the world. We are New York, Paris, Berlin. We are directional. We lead. We are freedom seekers. We aspire. We are full of contradictions …...and potential. We experiment. We dont want to be limited ….or labelled. We are strivers and dreamers. We self start. We get it on our own. We are travellers and taste makers. We are bosses and business women. We are creatives and professionals. We are logical and intelligent and loving. We read and see and know. We stand out. We are unique. We are loyal. We are all about our people. We stand true. We love art design and beautiful interesting things. We have to feel it. We have never ending lists. We live music. We explore every emotional terrain within and without. Our Story We created The Velvet North to speak to the woman who has as Velvet North as she does passions. We speak to those that are frustrated at being boxed in - we know you, we see you, that woman that can be feminine and edgy, urban and elegant, bold and understated, glamorous yet minimal. Our brand speaks to that multifaceted woman, you, and is a perfect mash-up of all of her sides. This is a new way to dress for our times We created this for those who appreciate fashion as a living art an important and vital mode of expression. We wanted to help women feel more free, more expressive and more than ever able to communicate all of their moods, all of their gifts through the medium of wearable but exciting contemporary urban luxury. We keep things simple but ever changing. Our clothes are versatile yet inspired. That are what you need for your lifestyle and allows you to be all of the women you are. We give you room to constantly evolve and expand their boundaries and experience new emotional terrain through the themes and moods of every new collection. We are a London bred brand, but are not afraid to explore many moods - the soft and feminine but also the dark and edgy - even if they appear contradictory. Ultimately we want to leave you with a wardrobe of collectible pieces that will provide you in years to come with your life's fashion soundtrack, markers made out of fabric of all your life's memories and milestones. Our vision throughout is to allow you to experience and express your Velvet North through beautiful fashion. Design Ethos We like beautiful clothes that are well made fit well are distinctive but incredibly wearable. We are Made in England and take quality fabric and finishing seriously. We make clothes that uniquely combine urban edge with feminine elegance and a luxe understated glamour. We have a signature but we challenge ourselves with every new collection to find new emotional terrain connect with a new part of our journey communicate a mood or experience that moves us feel around a concept/ Today we may be dark, tomorrow light. We are inspired by everything art, culture, politics, and feeling.Everything that touches your life becomes part of our work. Experimentation is the whole point and why we do this. We aim to delight and challenge you. Get you to try something new. Maybe even feel something new. We want to talk to you through fashion. Stay connected @thevelvetnorth

Target Market(s)

25 year old women.

Industry/Entity Type

Fashion

Contact Information for Business Card

Mara Quill
Creative Director
mara@thevelvetnorth.com

Mara Quill
Creative Director
mara@thevelvetnorth.com
07831620957

Logo Text

No text only a symbol

Number of Pages Required

5+ page

Font styles to use
Sans Serif

Colors

Designer to choose colors to be used in the design.

Requirements
Must have
• My standard colours are grey black and white (see existing webpage) and so to bring in a glamour quotient one idea is use of metallics such as silver or neon.
Nice to have
• to tie the stationary and web together with the logo - same colours and themes - repeating symbols or patterns.

```html
<!DOCTYPE html>
<html lang="en">
<head>
<meta charset="utf-8">
<title>The Velvet North — Home</title>
<link href="https://fonts.googleapis.com/css2?family=Josefin+Sans:wght@300;400;600&family=Oswald:wght@400;500&family=Montserrat:wght@400;600;700&display=swap" rel="stylesheet">
<style>
  :root {
    --page: #ffffff;
    --ink: #2a2a2a;
    --muted: #7a7a7a;
    --gold: #c7a15b;
    --tile: #efe9e5;
    --tile-deep: #e2dad3;
    --navy: #23263a;
    --sky: #9fb3d4;
    --hero-light: #e4e0d8;
    --hero-mid: #bdb6aa;
    --hero-warm: #8a7a68;
  }
  * { box-sizing: border-box; margin: 0; padding: 0; }
  html, body { width: 1200px; height: 900px; overflow: hidden; background: var(--page); }
  body { position: relative; font-family: "Montserrat", sans-serif; color: var(--ink); }

  /* Header */
  .site-header { position: absolute; left: 0; top: 0; width: 1200px; height: 78px; display: flex; align-items: center; padding: 0 60px; }
  .brand { display: flex; align-items: center; gap: 10px; }
  .brand-square { width: 9px; height: 9px; background: var(--ink); }
  .brand-name { font-family: "Josefin Sans", sans-serif; font-weight: 400; font-size: 22px; letter-spacing: 2px; color: var(--ink); }
  .main-nav { display: flex; gap: 34px; margin-left: 110px; }
  .main-nav a { font-family: "Josefin Sans", sans-serif; font-size: 14px; color: var(--ink); text-decoration: none; padding-bottom: 4px; }
  .main-nav a.is-active { color: var(--gold); border-bottom: 2px solid var(--gold); }
  .header-tools { margin-left: auto; display: flex; align-items: center; gap: 18px; }
  .header-tools svg { width: 17px; height: 17px; stroke: var(--ink); fill: none; stroke-width: 1.6; }
  .cart { position: relative; display: flex; }
  .cart-badge { position: absolute; top: -5px; right: -6px; width: 9px; height: 9px; border-radius: 50%; background: var(--gold); }
  .login { display: flex; align-items: center; gap: 6px; font-family: "Josefin Sans", sans-serif; font-size: 14px; }

  /* Hero */
  .hero { position: absolute; left: 0; top: 78px; width: 1200px; height: 420px; overflow: hidden; }
  .hero-photo { position: absolute; inset: 0;
    background:
      radial-gradient(ellipse 160px 210px at 800px 330px, var(--sky) 0%, rgba(159,179,212,0.5) 55%, rgba(159,179,212,0) 100%),
      radial-gradient(ellipse 120px 150px at 800px 130px, var(--hero-warm) 0%, rgba(138,122,104,0) 100%),
      linear-gradient(100deg, var(--hero-light) 0%, var(--hero-mid) 40%, #cfc8bd 65%, var(--hero-light) 100%); }
  .hero-copy { position: absolute; left: 70px; top: 140px; color: #fff; }
  .hero-kicker { font-size: 12px; font-weight: 600; letter-spacing: 0.5px; }
  .hero-title { font-family: "Oswald", sans-serif; font-weight: 400; font-size: 46px; line-height: 1.2; margin: 6px 0 22px; }
  .btn-gold { display: inline-block; background: var(--gold); color: #fff; font-size: 11px; font-weight: 600; padding: 9px 18px; }
  .slider-dots { position: absolute; left: 70px; bottom: 38px; display: flex; gap: 6px; }
  .slider-dots span { width: 22px; height: 3px; background: rgba(255,255,255,0.75); }
  .slider-dots span.is-current { background: var(--gold); }

  /* Collections */
  .collections { position: absolute; left: 0; top: 498px; width: 1200px; height: 402px; }
  .tile-photo { position: absolute; background: linear-gradient(180deg, var(--tile) 0%, var(--tile-deep) 100%); }
  .tile-photo.is-dark { background:
      radial-gradient(ellipse 34% 36% at 50% 58%, var(--navy) 0%, rgba(35,38,58,0.35) 70%, rgba(35,38,58,0) 100%),
      linear-gradient(180deg, var(--tile) 0%, var(--tile-deep) 100%); }
  .tile-photo.is-grey { background:
      radial-gradient(ellipse 30% 40% at 50% 55%, #9a9a9c 0%, rgba(154,154,156,0.3) 70%, rgba(154,154,156,0) 100%),
      linear-gradient(180deg, var(--tile) 0%, var(--tile-deep) 100%); }
  .tile-photo.is-light { background:
      radial-gradient(ellipse 30% 34% at 50% 50%, #ffffff 0%, rgba(255,255,255,0) 100%),
      linear-gradient(180deg, #f3efeb 0%, var(--tile-deep) 100%); }
  .feature-label { position: absolute; left: 320px; top: 140px; font-size: 11px; font-weight: 600; color: var(--gold); line-height: 1.4; letter-spacing: 0.5px; }
  .product-card { position: absolute; }
  .product-type { font-size: 11px; font-weight: 700; letter-spacing: 1px; color: var(--ink); }
  .product-name { font-size: 10px; color: var(--muted); margin: 4px 0 8px; white-space: nowrap; }
  .btn-shop { display: inline-block; background: var(--gold); color: #fff; font-size: 9px; font-weight: 600; padding: 5px 10px; }
  .btn-shop.is-outline { background: transparent; color: var(--gold); border-bottom: 1px solid var(--gold); padding: 4px 2px; }
  .tops-band { position: absolute; left: 620px; top: 232px; width: 480px; height: 150px; background: var(--tile); }
</style>
</head>
<body>

<header class="site-header">
  <div class="brand">
    <span class="brand-square"></span>
    <span class="brand-name">THE VELVET NORTH</span>
  </div>
  <nav class="main-nav">
    <a href="#" class="is-active">Home</a>
    <a href="#">About Us</a>
    <a href="#">Collections</a>
    <a href="#">Blog</a>
    <a href="#">Contact Us</a>
  </nav>
  <div class="header-tools">
    <svg viewBox="0 0 20 20" aria-label="Search"><circle cx="8.5" cy="8.5" r="6"/><line x1="13" y1="13" x2="18" y2="18"/></svg>
    <svg viewBox="0 0 20 20" aria-label="Wishlist"><path d="M10 17 L3 10 A4 4 0 0 1 10 4.5 A4 4 0 0 1 17 10 Z"/></svg>
    <span class="cart">
      <svg viewBox="0 0 20 20" aria-label="Cart"><path d="M2 3 H5 L7 13 H16 L18 6 H6"/><circle cx="8" cy="17" r="1.3"/><circle cx="15" cy="17" r="1.3"/></svg>
      <span class="cart-badge"></span>
    </span>
    <span class="login">
      <svg viewBox="0 0 20 20" aria-hidden="true"><circle cx="10" cy="7" r="4"/><path d="M3 18 C4 13 16 13 17 18"/></svg>
      Login
    </span>
  </div>
</header>

<section class="hero">
  <div class="hero-photo" role="img" aria-label="Slideshow photograph of a smiling woman in a straw hat and blue sundress on a sunny balcony"></div>
  <div class="hero-copy">
    <p class="hero-kicker">Fashion Lookbook</p>
    <h1 class="hero-title">Sale Up to 50% Off</h1>
    <span class="btn-gold">Shop by Collections</span>
  </div>
  <div class="slider-dots"><span></span><span class="is-current"></span><span></span><span></span></div>
</section>

<section class="collections">
  <div class="tile-photo is-grey" style="left:100px; top:30px; width:200px; height:270px;" role="img" aria-label="Model in a grey sleeveless shift dress"></div>
  <p class="feature-label">Best<br>Collections</p>

  <div class="tile-photo is-dark" style="left:440px; top:30px; width:130px; height:170px;" role="img" aria-label="Model in a navy short-sleeved dress"></div>
  <div class="product-card" style="left:585px; top:80px;">
    <p class="product-type">OUTERWEAR</p>
    <p class="product-name">Silk Wrap Jacket</p>
    <span class="btn-shop">Shop Now!</span>
  </div>

  <div class="tile-photo is-dark" style="left:790px; top:30px; width:130px; height:170px;" role="img" aria-label="Model in a navy culotte jumpsuit"></div>
  <div class="product-card" style="left:935px; top:80px;">
    <p class="product-type">DRESSES</p>
    <p class="product-name">Wide Leg Pinafore</p>
    <span class="btn-shop is-outline">Shop Now!</span>
  </div>

  <div class="tile-photo is-light" style="left:350px; top:220px; width:130px; height:165px;" role="img" aria-label="Model in a white shirt dress"></div>
  <div class="product-card" style="left:495px; top:270px;">
    <p class="product-type">DRESSES</p>
    <p class="product-name">White Shirt Dress</p>
    <span class="btn-shop is-outline">Shop Now!</span>
  </div>

  <div class="tops-band"></div>
  <div class="tile-photo is-light" style="left:620px; top:232px; width:160px; height:150px;" role="img" aria-label="Model in a white cami top and black trousers"></div>
  <div class="product-card" style="left:810px; top:270px;">
    <p class="product-type">TOPS</p>
    <p class="product-name">Ribbed Cami Top</p>
    <span class="btn-shop is-outline">Shop Now!</span>
  </div>
  <div class="tile-photo is-light" style="left:940px; top:232px; width:160px; height:150px;" role="img" aria-label="Back view of a model in a white strappy top"></div>
</section>

</body>
</html>
```